依頼詳細
恥を忍んで書きます。主にシステム側を得意とする自分が、デザインも含めた案件を引き受けてしまい、トップページのデザイン案として以下の2つを作成したところ、クオリティ不足を言い渡されてしまいました。ごもっともだと自覚しています。
http://pelmo.jp/up/tarucs-green.jpg
http://pelmo.jp/up/tarucs-blue.jpg

上記のつたないデザイン案で問題ないのはページ内の「要素」だけですので、デザインのブラッシュアップ、または抜本的なリフレッシュをお願いします。ひとまずトップページ画像だけで大丈夫です。

なお、過去にWordPressテンプレートサイトのデザインに企業名を充てただけの以下のデザインは気に入っていただいています。このテイストをまるごと使ってもかまいません。
http://templates.vorlinquest.com/template_number/live_demo.asp?TemplateID=41938
http://pelmo.jp/up/tarucs-template.jpg

できれば9/2(月)いっぱいくらいで先方に提示したいと考えていて、無謀なスケジュールなので、手を上げていただける方の労力ができるだけ無駄にならないようにしたいです。
サイトURL
http://www.tarucs.co.jp/
ページ数
1ページ
希望イメージ
シンプル 複雑
単色 カラフル
暗い 明るい
日常 高級
遊び心 厳粛
未来的 伝統的
女性的 男性的
希望する色
緑ないし青ベースで、黄と赤をアクセントにとの先方の希望です。
納品ファイル
• 高解像度JPG (.jpg)
• イラストレーター形式 (.ai)
補足説明
ここにメアドを書いていいのかわかりませんが、詳細はお気軽にお問い合わせください。
ご質問など承りますし、素材などもお送りいたします。
mあっとpelmo.jp
追記補足です。
トップページのメイン画像は、
よくある複数パターンの切り替え式(時間経過かクリック)の予定です。
とりあえず今回のご提案では「すばらしい自然を未来の子供たちに…」の
メッセージのもので大丈夫ですが、切り替え式となることをご考慮ください。
これから提案をご予定の方々には申し訳ありません。

過去にクライアントに気に入っていただいたWordPressテンプレートのイメージをうまく活かして、きれいにまとめていただいたdorusan72様に決めさせていただきました。テンプレートのイメージに沿わせるべきか、オリジナリティを出すほうがいいかは、わたしも判断に迷うところでしたが、最終的には先方に選んでいただきました。
青バージョンとして色のイメージを参考にさせていただいたmepolt様、そしてWordPress構築を意識してデザインしていただいたranpu様を次点として選ばせていただきました。

短期のスケジュールだった上に途中でほぼ即決の方向で調整させていただきまして、ランサーの皆様にはご迷惑おかけしてしまいました。
初めてのハルモワークスの利用でしたが、こんなに短期間でクオリティの高いご提案がいただけて大変感激しています。もちろん、次に利用させていただくときはこんなスケジュールにならないようにしたいと思います。
ご提案に至らなかった皆様も含めまして、ありがとうございました。

```html
<!DOCTYPE html>
<html lang="ja">
<head>
<meta charset="utf-8">
<title>TARUCS</title>
<link rel="stylesheet" href="https://fonts.googleapis.com/css2?family=Noto+Sans+JP:wght@400;700&display=swap">
<style>
:root{
  --green:#3f9a35;
  --green-dark:#2c7a25;
  --green-light:#8cc63f;
  --sky-top:#4f93cc;
  --sky-mid:#8fbde2;
  --sky-bottom:#e4eef7;
  --ink:#333;
  --muted:#777;
  --line:#d6d6d6;
  --panel:#f4f4f4;
  --yellow:#f2c81a;
  --red:#d9432c;
}
*{box-sizing:border-box;margin:0;padding:0}
html,body{width:755px;height:1200px;overflow:hidden;background:#fff}
body{font-family:"Noto Sans JP",sans-serif;color:var(--ink);font-size:10px;position:relative}

.global-nav{position:absolute;top:0;left:0;width:755px;height:30px;background:var(--green);display:flex;padding-left:10px;border-bottom:3px solid var(--green-dark)}
.global-nav a{color:#fff;text-decoration:none;font-size:11px;padding:0 18px;line-height:28px;border-right:1px solid rgba(255,255,255,.4);letter-spacing:.05em}

.site-title{position:absolute;top:44px;left:0;width:755px;text-align:center}
.site-title .tagline{font-size:8px;color:var(--muted);letter-spacing:.1em}
.site-title .name{font-weight:700;font-size:32px;color:var(--green);letter-spacing:.1em;line-height:1.3}

.hero{position:absolute;top:128px;left:0;width:755px;height:488px;overflow:hidden}
.hero-photo{position:absolute;inset:0;background:linear-gradient(180deg,var(--sky-top) 0%,var(--sky-mid) 50%,var(--sky-bottom) 100%)}
.hero-copy{position:absolute;top:40px;left:0;width:755px;text-align:center;color:#fff}
.hero-copy .sub{font-size:11px;letter-spacing:.1em}
.hero-copy .main{display:inline-block;margin-top:6px;font-size:21px;font-weight:700;padding:4px 40px;background:rgba(20,50,80,.35);letter-spacing:.05em}
.hero-arrow{position:absolute;top:220px;width:26px;height:26px;border-radius:50%;background:rgba(255,255,255,.85);display:flex;align-items:center;justify-content:center}
.hero-arrow.prev{left:12px}.hero-arrow.next{right:12px}
.hero-dots{position:absolute;bottom:16px;left:0;width:755px;display:flex;justify-content:center;gap:28px}
.hero-dots span{width:9px;height:9px;border-radius:50%;background:rgba(255,255,255,.7)}
.hero-dots span.on{background:var(--yellow)}
.hero-rule{position:absolute;top:616px;left:0;width:755px;height:6px;background:var(--green)}

.banners{position:absolute;top:668px;left:38px;width:152px}
.banner{height:60px;margin-bottom:7px;display:flex;align-items:flex-end;padding:5px 6px;color:#fff;font-weight:700;font-size:10px;line-height:1.25;text-shadow:0 1px 2px rgba(0,0,0,.35)}
.banner.lecture{background:linear-gradient(135deg,#4f9e2f,#a9d46c)}
.banner.workshop{background:linear-gradient(135deg,#d8c58e,#e9a93a);color:var(--red);text-shadow:none;align-items:center;justify-content:center;text-align:center}
.banner.event{background:linear-gradient(135deg,#b8362a,#ec7a3a)}

.topics{position:absolute;top:668px;left:205px;width:350px;height:200px;background:var(--panel);border:1px dashed var(--line);padding:12px 14px}
.topics h2{font-size:13px;font-weight:700;letter-spacing:.05em;border-bottom:1px solid var(--line);padding-bottom:4px;margin-bottom:6px}
.topics ul{list-style:none}
.topics li{display:flex;font-size:8px;line-height:19px;color:#555;border-bottom:1px dotted var(--line)}
.topics li time{width:58px;color:var(--muted)}

.contact{position:absolute;top:668px;left:582px;width:135px;border:1px solid var(--line)}
.contact .head{background:#888;color:#fff;font-size:7px;text-align:center;line-height:14px}
.contact .tel{font-size:13px;color:var(--green-dark);font-weight:700;padding:4px 8px 0}
.contact .mail{display:flex;align-items:center;gap:6px;font-size:11px;padding:2px 8px 6px}
.badge{position:absolute;left:582px;width:135px;height:22px}
.badge.one{top:826px;background:#3b8f3a}
.badge.two{top:854px;background:#9dcf4e}

.footer-nav{position:absolute;top:990px;left:38px;width:680px;height:150px;display:flex;border-top:1px solid var(--line);border-bottom:1px solid var(--line)}
.footer-col{flex:1;padding:10px 8px;border-right:1px dotted var(--line)}
.footer-col:last-child{border-right:none}
.footer-col h3{font-size:10px;font-weight:700;margin-bottom:6px;white-space:nowrap;letter-spacing:-.02em}
.footer-col li{list-style:none;font-size:8px;line-height:16px;color:#555}
.footer-col li::before{content:"▸ ";color:var(--green)}
.social{display:flex;gap:8px;margin-top:4px}
.social span{width:22px;height:22px;border-radius:50%;background:#555}
.copyright{position:absolute;top:1152px;left:38px;width:680px;display:flex;justify-content:space-between;font-size:8px;color:var(--muted)}
.copyright nav a{color:var(--muted);text-decoration:none;margin-left:12px}
</style>
</head>
<body>
<nav class="global-nav">
  <a>トップ</a><a>会社概要</a><a>コンサルティング事業</a><a>新エネルギー事業</a><a>ものづくり事業</a>
</nav>

<header class="site-title">
  <p class="tagline">すばらしい自然を未来の子供たちに残すために</p>
  <p class="name">TARUCS</p>
</header>

<section class="hero">
  <div class="hero-photo" role="img" aria-label="青空の下に立つ白い風力発電機の写真"></div>
  <div class="hero-copy">
    <p class="sub">すばらしい自然を未来の子供たちに残すために</p>
    <p class="main">あたらしいエネルギー会社を私たちと一緒に作りませんか？</p>
  </div>
  <span class="hero-arrow prev"><svg width="8" height="10" viewBox="0 0 8 10"><path d="M6 1 2 5l4 4" fill="none" stroke="#555" stroke-width="1.6"/></svg></span>
  <span class="hero-arrow next"><svg width="8" height="10" viewBox="0 0 8 10"><path d="M2 1l4 4-4 4" fill="none" stroke="#555" stroke-width="1.6"/></svg></span>
  <div class="hero-dots"><span class="on"></span><span></span><span></span><span></span><span></span></div>
</section>
<div class="hero-rule"></div>

<aside class="banners">
  <div class="banner lecture" role="img" aria-label="講座・シンポジウムの案内バナー写真">講座・シンポジウム</div>
  <div class="banner workshop" role="img" aria-label="エネルギーワークショップの案内バナー写真">レッツ エネルギー<br>ワークショップ</div>
  <div class="banner event" role="img" aria-label="イベント案内のバナー写真">イベント情報</div>
</aside>

<section class="topics">
  <h2>TOPICS</h2>
  <ul>
    <li><time>2013.08.28</time>新エネルギー講座の受講者募集を開始しました</li>
    <li><time>2013.08.20</time>ワークショップ開催報告を掲載しました</li>
    <li><time>2013.08.09</time>夏季休業のお知らせ</li>
    <li><time>2013.07.30</time>太陽光発電の導入事例を更新しました</li>
    <li><time>2013.07.18</time>シンポジウムの資料を公開しました</li>
    <li><time>2013.07.05</time>ものづくり事業の新製品を紹介します</li>
    <li><time>2013.06.21</time>ホームページをリニューアルしました</li>
  </ul>
</section>

<aside class="contact">
  <p class="head">お問い合わせ・ご相談はお気軽に</p>
  <p class="tel">TEL 076-418-2205</p>
  <p class="mail">
    <svg width="16" height="11" viewBox="0 0 16 11"><rect x=".5" y=".5" width="15" height="10" fill="none" stroke="#3f9a35"/><path d="M.5 .5 8 6l7.5-5.5" fill="none" stroke="#3f9a35"/></svg>Mail
  </p>
</aside>
<div class="badge one" role="img" aria-label="加盟団体バッジ"></div>
<div class="badge two" role="img" aria-label="認定バッジ"></div>

<footer>
  <nav class="footer-nav">
    <div class="footer-col"><h3>トップ</h3><ul><li>講座・シンポジウム</li><li>活動報告</li><li>お知らせ</li></ul></div>
    <div class="footer-col"><h3>会社概要</h3><ul><li>企業情報</li><li>代表挨拶</li><li>沿革</li><li>連絡の窓口</li></ul></div>
    <div class="footer-col"><h3>コンサルティング事業</h3><ul><li>概要</li></ul></div>
    <div class="footer-col"><h3>新エネルギー事業</h3><ul><li>太陽光</li><li>風力</li><li>水力</li><li>大地</li><li>新技術</li></ul></div>
    <div class="footer-col"><h3>ものづくり事業</h3></div>
    <div class="footer-col"><h3>Join Us !</h3><div class="social"><span></span><span></span></div></div>
  </nav>
  <div class="copyright">
    <p>Copyright © 2013 TARUCS. All Rights Reserved.</p>
    <nav><a>お問い合わせ</a><a>プライバシーポリシー</a></nav>
  </div>
</footer>
</body>
</html>
```